Redesign Our Retail Site (Theme Customization)

We currently have an online store that needs a new design. This design should be based on the Vendora Theme for Cartwell. Here is our current website:

http://www.lunaquilts.example

We would like to convert it to the Vendora theme:

http://www.vendora.example

The Vendora theme has a simple-to-use control panel that allows you to control all fonts, colors, backgrounds images, and many other things. There is also 1 css stylesheet for doing in-depth customization. It's really easy to use.

For those serious about this project, please contact me and I will send you the Vendora theme so that you can customize it. You will need to install Cartwell to do this.

We need someone who can give our website some CSS-love. Also, this person needs to be able to design a few main ads, a new background, brush up our logo, and make the color scheme nice and pretty. Make everything tie together.

We will need 3 main ads for the main banner (920 x 320 pixels each). These should say:

"Olympic queen sheets on sale now"
"Twin XL sheets on sale now"
"California King sheets on sale now"

We have already transferred all the product and category data into an Cartwell/Vendora install here:

http://www.lunaquilts.example/new

If you don't want to install Cartwell/Vendora just to submit a design, you may just take screen shot of that page, change it up, add a main ad, make it look good, and send it to me if you'd like to submit a design. Eventually, anything submitted this way needs to be transferred to Vendora though.

Thank you very much.

Regards,

Dane Holvik
LunaQuilts.example
-
Questions? SKYPE ME! - "chatdaneholvik"

Target Market(s)

Adults in USA between the ages of 18 to 40

Industry/Entity Type

Store

Requirements
Must have
• Must be elgant and lovely. Must compliment our name "Luna Quilts" and be playful.

```html
<!DOCTYPE html>
<html lang="en">
<head>
<meta charset="utf-8">
<title>Luna Quilts – Luxury Bed Sheets &amp; Bedding</title>
<link href="https://fonts.googleapis.com/css2?family=Ubuntu:wght@300;400&family=PT+Sans:wght@400;700&display=swap" rel="stylesheet">
<style>
:root{
  --frame:#b9e2ea;
  --page:#ffffff;
  --blue:#2ba6d6;
  --nav:#1d79b8;
  --green:#6aa812;
  --ink:#333333;
  --body:#4a4a4a;
  --muted:#777777;
  --panel:#f3f3f3;
  --rule:#5fc0dd;
  --cart:#e0731b;
}
*{box-sizing:border-box;margin:0;padding:0}
html,body{width:1200px;height:2297px;overflow:hidden}
body{background:var(--frame);font-family:"PT Sans",Arial,sans-serif;color:var(--body);position:relative}
.page{position:absolute;left:14px;top:0;width:1170px;height:2268px;background:var(--page)}
.page>*{position:absolute}
h1,h2,h3{font-family:"Ubuntu",Arial,sans-serif;font-weight:300;color:var(--ink)}
a{color:inherit;text-decoration:none}

.logo{left:52px;top:44px;width:210px;text-align:center}
.logo-mark{display:inline-block;width:62px;height:40px;border-radius:50%;background:var(--green);vertical-align:middle}
.logo-name{display:block;font-family:"PT Sans",sans-serif;font-weight:700;font-size:22px;color:var(--green);margin-top:2px}
.logo-tag{display:block;font-size:16px;color:#555;margin-top:10px}

.cart{right:36px;top:40px;font-size:17px;color:var(--cart)}
.cart span{color:var(--ink)}
.account-links{right:36px;top:78px;font-size:15px;color:#555;word-spacing:2px}
.account-links i{font-style:normal;color:#aaa;margin:0 12px}
.search{left:839px;top:120px;width:295px;height:34px;border:1px solid #cfe9f3;border-radius:17px;box-shadow:0 2px 4px rgba(43,166,214,.25);font-size:14px;color:var(--blue);padding:7px 14px}
.search-go{left:1100px;top:116px;width:40px;height:40px;border-radius:50%;background:var(--blue);color:#fff;font-size:16px;text-align:center;line-height:38px}

.dots{left:28px;width:1134px;border-top:2px dotted var(--rule)}
.nav{left:28px;top:194px;width:1134px;height:30px;font-family:"Ubuntu",sans-serif;font-size:17px;color:var(--nav)}
.nav a{position:absolute;top:2px}
.nav b{position:absolute;top:2px;width:1px;height:24px;background:#b7d6e6}

.banner{left:7px;top:259px;width:1157px;height:410px;background:linear-gradient(120deg,#8c82c2 0%,#b1a8dc 30%,#d8d3ee 55%,#9a90cb 75%,#e6e3f2 100%)}
.banner-edge{left:7px;top:252px;width:1157px;height:10px;background:linear-gradient(135deg,var(--page) 50%,transparent 50%) 0 0/14px 10px,linear-gradient(225deg,var(--page) 50%,transparent 50%) 0 0/14px 10px}
.banner-copy{left:596px;top:456px;width:530px;height:142px;background:#fff;border:1px solid #d0d0d0;box-shadow:0 1px 4px rgba(0,0,0,.25);padding:20px 26px}
.banner-copy h2{font-size:33px;color:#333;margin-bottom:12px}
.banner-copy p{font-size:14px;line-height:22px;color:var(--nav)}
.slider-dots{left:21px;top:638px;display:flex;gap:5px}
.slider-dots span{width:20px;height:14px;background:#fff;opacity:.9}

.welcome{left:32px;top:700px;width:1112px}
.welcome h1{font-size:25px;margin-bottom:14px}
.welcome p{font-size:13.4px;line-height:21.5px;margin-bottom:18px}

.section-title{font-size:24px;color:var(--ink)}
.latest-title{left:34px;top:978px}
.products{left:25px;top:1020px;display:flex;gap:15px}
.product{width:213px}
.product .thumb{height:192px;border:1px solid #ddd;padding:5px;background:#fff;box-shadow:0 1px 3px rgba(0,0,0,.1)}
.product .thumb div{width:100%;height:100%}
.product .name{font-size:16px;color:var(--green);margin-top:8px}
.product .price{font-size:24px;color:var(--green);margin-top:-2px}

.catalog{left:18px;top:1338px;width:1131px;height:306px;background:var(--panel)}
.catalog>*{position:absolute}
.catalog h3{font-size:22px;top:22px}
.catalog ul{list-style:none;font-size:13.6px;color:#444}
.catalog li{height:29.5px;padding-left:16px;position:relative}
.catalog li::before{content:"";position:absolute;left:0;top:5px;width:6px;height:6px;border-right:1.5px solid #888;border-top:1.5px solid #888;transform:rotate(45deg)}
.catalog ul.large{font-size:15px}

.tips-title{left:34px;top:1668px}
.tips-divider{left:590px;top:1715px;width:1px;height:365px;background:#ddd}
.tip{width:500px;font-size:13.4px;line-height:21px;color:#444;padding-left:60px}
.tip .num{position:absolute;left:0;top:-2px;width:38px;height:38px;border-radius:50%;background:var(--blue);color:#fff;font-size:21px;text-align:center;line-height:38px;font-family:"Ubuntu",sans-serif}

.footer-edge{left:0;top:2130px;width:1170px;height:30px;background:linear-gradient(#fff,#f1f1f1);}
.footer-edge::before{content:"";position:absolute;left:0;top:0;width:100%;height:8px;background:linear-gradient(135deg,#e4e4e4 50%,transparent 50%) 0 0/12px 8px,linear-gradient(225deg,#e4e4e4 50%,transparent 50%) 0 0/12px 8px}
.footer-links{left:28px;top:2166px;font-size:13.6px;color:#444}
.footer-links i{font-style:normal;color:#999;margin:0 10px}
.copyright{left:28px;top:2207px;font-size:13px;color:#444}
.payments{left:858px;top:2168px;display:flex;gap:8px}
.payments span{width:48px;height:30px;border:1px solid #c8c8c8;border-radius:3px;background:linear-gradient(#ffffff,#e8e8e8)}
.payments span.dark{background:#1e3b86;border-color:#1e3b86}
</style>
</head>
<body>
<div class="page">

  <a class="logo" href="#"><span class="logo-mark"></span><span class="logo-name">Luna Quilts</span><span class="logo-tag">Luxury Bed Sheets &amp; Bedding</span></a>

  <div class="cart">Your Cart <span>&nbsp;0 itmes</span></div>
  <div class="account-links"><a href="#">Log In</a><i>|</i><a href="#">Sign up</a><i>|</i><a href="#">Free Shipping</a></div>
  <div class="search">search here..</div>
  <div class="search-go">go</div>

  <div class="dots" style="top:181px"></div>
  <nav class="nav">
    <a href="#" style="left:44px">Home</a><b style="left:128px"></b>
    <a href="#" style="left:162px">My Account</a><b style="left:282px"></b>
    <a href="#" style="left:322px">Learning Center</a><b style="left:472px"></b>
    <a href="#" style="left:514px">Shopping Cart</a><b style="left:652px"></b>
    <a href="#" style="left:692px">Create Account</a><b style="left:836px"></b>
    <a href="#" style="left:880px">Contact</a>
  </nav>
  <div class="dots" style="top:232px"></div>

  <div class="banner" role="img" aria-label="Bedroom photo: lavender duvet and pillows with embroidered purple flowers"></div>
  <div class="banner-edge"></div>
  <div class="banner-copy">
    <h2>Luxury Bed Sheets &amp; Bedding</h2>
    <p>Where do worries sink away, washed over by serenity? Where does comfort sedate the stress of life? Where can joy and laughter be shared no matter what</p>
  </div>
  <div class="slider-dots"><span></span><span></span><span></span><span></span><span></span></div>

  <section class="welcome">
    <h1>Welcome to Luna Quilts</h1>
    <p>Where do worries sink away, washed over by serenity? Where does comfort sedate the stress of life? Where can joy and laughter be shared no matter what you're wearing? Where do you let yourself go completely and utterly? You surrender to your bed each day, in the wash of night, when time resets itself for another go-round. And not just your bed, but everything on and around it.</p>
    <p>Try a Premiere down pillow!At Luna Quilts, we provide solutions for all your bedding needs. You owe yourself the tranquility and nurturing rest that our premium bedding products facilitate. You deserve the soothing comfort of our quality bedding and sheets. You can sleep wrapped in bedding fit for royalty. You can burrow under one of our plush comforters. You can enhance your existing mattress with our choice of mattress pads. Or, perfect your sanctuary's decor with one of our bedskirts. You'll find fitting accessories for nearly every bed size at Luna Quilts.</p>
  </section>

  <div class="dots" style="top:953px"></div>

  <h2 class="section-title latest-title">Latest Beddings</h2>
  <div class="products">
    <div class="product"><div class="thumb"><div role="img" aria-label="Cream bedding on a wooden bed" style="background:linear-gradient(135deg,#8a6a4a,#e9e2d4 55%,#c9b79c)"></div></div><div class="name">Beeding sheet name</div><div class="price">$ 250</div></div>
    <div class="product"><div class="thumb"><div role="img" aria-label="Pink nursery with white crib" style="background:linear-gradient(135deg,#f4c9d6,#fbeef2 50%,#e79ab4)"></div></div><div class="name">Beeding sheet name</div><div class="price">$ 250</div></div>
    <div class="product"><div class="thumb"><div role="img" aria-label="White sheets with purple floral print" style="background:linear-gradient(135deg,#d9d3e4,#f7f6fa 50%,#b48fc9)"></div></div><div class="name">Beeding sheet name</div><div class="price">$ 250</div></div>
    <div class="product"><div class="thumb"><div role="img" aria-label="Brown patterned quilt with pink border" style="background:linear-gradient(135deg,#e6a9cf,#6d5642 40%,#3a2a20 80%,#e6a9cf)"></div></div><div class="name">Beeding sheet name</div><div class="price">$ 250</div></div>
    <div class="product"><div class="thumb"><div role="img" aria-label="Dark brown and orange bedding set" style="background:linear-gradient(135deg,#2c1a12,#7a3d1e 50%,#3a2417)"></div></div><div class="name">Beeding sheet name</div><div class="price">$ 250</div></div>
  </div>

  <div class="dots" style="top:1301px"></div>

  <section class="catalog">
    <h3 style="left:44px">Most Popluar Sellings</h3>
    <ul style="left:44px;top:75px">
      <li>Hard-Side Waterbed Sheets</li><li>Soft-Side Waterbed Sheets</li><li>Flat or Fitted Sheets Only</li><li>Bed In A Bag Sets</li><li>Extra Deep Pocket Sheets</li><li>Pillows</li><li>Pillow Cases and Shams</li>
    </ul>
    <ul style="left:282px;top:75px">
      <li>Bamboo Sheets</li><li>Flannel Sheets</li><li>Microfiber Sheets</li><li>Extra Long Bedskirts</li><li>Throws</li><li>Miscellaneous</li>
    </ul>
    <h3 style="left:489px">Bedding by Size and Type</h3>
    <ul style="left:489px;top:73px">
      <li>California King Bedding</li><li>California King Sheets</li><li>California King Bed In A Bags</li><li>California King Bedskirts</li><li>California King Comforters</li><li>California King Duvet Covers</li><li>California King Mattress Pads</li>
    </ul>
    <ul style="left:715px;top:73px">
      <li>Full Bedding</li><li>Full Sheets</li><li>Full Bed In A Bags</li><li>Full Bedskirts</li><li>Full Comforters</li><li>Full Duvet Covers</li><li>Full Featherbeds</li>
    </ul>
    <ul class="large" style="left:888px;top:72px">
      <li>Full Mattress Pads</li><li>Full XL Bedding</li><li>Full XL Sheets</li><li>Full XL Bed In A Bags</li><li>Full XL Bedskirts</li><li>Full XL Mattress Pads</li>
    </ul>
  </section>

  <h2 class="section-title tips-title">Bed Sheet&nbsp; Buying Tips</h2>
  <div class="tips-divider"></div>

  <div class="tip" style="left:34px;top:1726px"><span class="num">1</span>Higher thread count sheets are usually softer, but aren't always the best. If you like a cooler, lighter sheet then shop in the 200 to 500 range. If you're looking for the ultimate in bedding softness, opt for a sateen weave.</div>
  <div class="tip" style="left:34px;top:1815px"><span class="num">2</span>If you're buying Olympic Queen sheets, consider buying just an Olympic Queen fitted sheet to save money if you already have a Queen sheet set.</div>
  <div class="tip" style="left:34px;top:1879px"><span class="num">3</span>The above also goes for California King sheets too. You may only have to buy a California King fitted sheet if you already have a King bedding set.</div>
  <div class="tip" style="left:34px;top:1948px"><span class="num">4</span>The type of cotton matters. Only look for Pima and Egyptian cotton as these are the best long-staple cottons.</div>
  <div class="tip" style="left:34px;top:2019px"><span class="num">5</span>Be sure to keep the thickness of your mattress in mind. Mattresses over 16 inches tall will require a "extra deep" sheet set.</div>

  <div class="tip" style="left:622px;top:1726px"><span class="num">6</span>Be wary of merchants who don't list the ply of their sheets. Having high plys is another way mills can take shortcuts to advertise their sheets as a higher thread count than they really are.</div>
  <div class="tip" style="left:622px;top:1820px"><span class="num">7</span>Not all blues are blue and not all reds are red. It's important to check with the supplier if you're wondering whether the color of one piece of bedding will match another.</div>
  <div class="tip" style="left:622px;top:1888px"><span class="num">8</span>Pure cotton sheets will be the softest and most breathable, and the natural cotton fibers will pull moisture (sweat) away from your body. Polycotton blends are more wrinkle resistant and moderately priced.</div>
  <div class="tip" style="left:622px;top:1973px"><span class="num">9</span>When selecting your sheets, consider buying at least one solid color sheet set to coordinate with your print bedding and other accessories.</div>
  <div class="tip" style="left:622px;top:2038px"><span class="num">10</span>Some sheet makers take shortcuts by only putting elastic on the top and bottom edge of the fitted sheet. Make sure the elastic goes all the way around the bottom edge, especially if you have a pillowtop.</div>

  <div class="footer-edge"></div>
  <nav class="footer-links"><a href="#">Home</a><i>|</i><a href="#">Learning Center</a><i>|</i><a href="#">Terms of Use</a><i>|</i><a href="#">Privacy</a><i>|</i><a href="#">Returns</a><i>|</i><a href="#">Contact Us</a><i>|</i><a href="#">Login</a></nav>
  <div class="copyright">© 2012 Luna Quilts &amp; Textile Inc.</div>
  <div class="payments" aria-label="Accepted payment methods"><span></span><span></span><span></span><span class="dark"></span><span></span></div>

</div>
</body>
</html>
```